New letterhead design for legal, public interest law firm

THIS IS FOR A LETTERHEAD DESIGN CONTEST , PLEASE REFRAIN FROM SUBMITTING JUST LOGO PROPOSALS AND BUSINESS CARD. LOGO AND BUSINESS CARD PROJECTS WILL BE AWARDED TO THE WINNER OF THE LETTERHEAD DESIGN.
Looking for a timeless, elegant and modern design for our letterhead and logo. Our website is www.lmrkvoa.org so you can incorporate the mission, vision and values into the design. As we also included a request for a NEW LOGO design, please be sure to include logo design options.
We are a public interest criminal defense organization that represents indigent people charged with federal crimes. Please weave the mission/vision/values and our practice area into the logo design.
Target Market(s)
Judges, clients, attorneys, family members of our clients.
Industry/Entity Type
Legal
Contact Information for Business Card
Include line for address, direct line, fax, email address, website address. Remember to incorporate NEW LOGO design.
Logo Text
Coastal Legal Advocacy Collective of the Western Valley
Requirements
Must have
- Please remember this project is also to design us a NEW LOGO. Please do not incorporate the existing logo into the new letterhead design.
Nice to have
- Nice to see some logo samples incorporating symbolism for justice, California specific imagery.
Should not have
- New logo should NOT have any traditional/typical legal related images (e.g., scales of justice, etc.)

```html
<!DOCTYPE html>
<html lang="en">
<head>
<meta charset="utf-8">
<title>Letterhead – Coastal Legal Advocacy Collective of the Western Valley</title>
<link rel="stylesheet" href="https://fonts.googleapis.com/css2?family=EB+Garamond:wght@400&family=Open+Sans:wght@400;700&display=swap">
<style>
  :root {
    --backdrop: #d9dcdd;
    --paper: #ffffff;
    --brand-blue: #1f64b0;
    --brand-blue-light: #4a8fd0;
    --brand-orange: #f39a2e;
    --rule-grey: #b9bbbd;
    --ink: #2b2b2b;
    --ink-soft: #555a5e;
  }
  * { box-sizing: border-box; margin: 0; padding: 0; }
  html, body {
    width: 1200px; height: 784px; overflow: hidden;
    background: var(--backdrop);
  }
  .canvas {
    position: relative; width: 1200px; height: 784px;
  }
  .letterhead {
    position: absolute; left: 330px; top: 42px;
    width: 541px; height: 700px;
    background: var(--paper);
    box-shadow: 0 6px 22px rgba(0,0,0,.18);
    overflow: hidden;
  }
  .corner-tab {
    position: absolute; left: 0; top: 0;
    width: 46px; height: 7px;
    background: var(--rule-grey);
  }
  .org-name {
    position: absolute; left: 58px; top: 28px;
    display: flex; align-items: center; gap: 10px;
  }
  .org-name__dot {
    width: 14px; height: 14px; border-radius: 50%;
    background: var(--brand-blue);
  }
  .org-name__text {
    font-family: "EB Garamond", serif;
    font-size: 14px; line-height: 1.1; color: var(--ink);
  }
  .top-rule {
    position: absolute; left: 180px; right: 0; top: 94px;
    height: 5px;
    background: linear-gradient(180deg, var(--brand-blue-light), var(--brand-blue));
  }
  .footer-art {
    position: absolute; left: 0; bottom: 0;
    width: 541px; height: 70px;
  }
  .contact-line {
    position: absolute; left: 10px; bottom: 52px;
    display: flex; align-items: center; gap: 4px;
    font-family: "Open Sans", sans-serif;
    font-size: 7.2px; color: var(--ink-soft); white-space: nowrap;
  }
  .contact-line__icon {
    width: 9px; height: 9px; border-radius: 50%;
    background: var(--brand-blue);
    display: inline-flex; align-items: center; justify-content: center;
  }
  .contact-line__item { display: inline-flex; align-items: center; gap: 3px; margin-right: 3px; }
  .web-address {
    position: absolute; right: 18px; bottom: 14px;
    font-family: "Open Sans", sans-serif; font-weight: 700;
    font-size: 17px; color: #ffffff; letter-spacing: .3px;
  }
</style>
</head>
<body>
<div class="canvas">
  <section class="letterhead">
    <div class="corner-tab"></div>

    <header class="org-name">
      <span class="org-name__dot"></span>
      <p class="org-name__text">Coastal Legal Advocacy Collective<br>of the Western Valley</p>
    </header>

    <div class="top-rule"></div>

    <svg class="footer-art" viewBox="0 0 541 70" aria-hidden="true">
      <polygon points="0,30 330,30 325,34 0,34" fill="var(--brand-orange)"/>
      <polygon points="0,40 150,40 146,44 0,44" fill="var(--brand-orange)"/>
      <polygon points="150,38 330,38 345,38 340,44 146,44" fill="var(--brand-blue)"/>
      <polygon points="0,46 345,46 355,70 0,70" fill="var(--brand-blue)"/>
      <polygon points="340,24 541,24 541,70 360,70" fill="var(--brand-blue)"/>
    </svg>

    <div class="contact-line">
      <span class="contact-line__item">
        <span class="contact-line__icon"><svg width="5" height="6" viewBox="0 0 10 12"><path d="M5 0a4 4 0 0 0-4 4c0 3 4 8 4 8s4-5 4-8a4 4 0 0 0-4-4z" fill="#fff"/></svg></span>
        0000 Example, Ste 135, California, 93103, United States
      </span>
      <span class="contact-line__item">
        <span class="contact-line__icon"><svg width="5" height="5" viewBox="0 0 10 10"><path d="M2 0l2 2-1 2 3 3 2-1 2 2-2 2C4 10 0 6 0 2z" fill="#fff"/></svg></span>
        (000) 000-0000
      </span>
      <span class="contact-line__item">
        <span class="contact-line__icon"><svg width="5" height="5" viewBox="0 0 10 10"><rect x="1" y="3" width="8" height="6" fill="#fff"/><rect x="3" y="0" width="4" height="3" fill="#fff"/></svg></span>
        (000) 000-0000
      </span>
      <span class="contact-line__item">
        <span class="contact-line__icon"><svg width="5" height="4" viewBox="0 0 10 8"><rect width="10" height="8" fill="#fff"/><path d="M0 0l5 4 5-4" stroke="#1f64b0" fill="none"/></svg></span>
        info@www.lmrkvoa.org
      </span>
    </div>

    <p class="web-address">www.lmrkvoa.org</p>
  </section>
</div>
</body>
</html>
```